Bin Sentry sales and convention information

The product is called the Bin Sentry. It's a commercial grade product designed to prevent dumpster drivers from damaging the enclosures the dumpsters are stored in by "Holding the Line Firm" from the drivers. They also prevent the dumpsters from being misplaced on the property as well as being moved by vandals during acts of arson. Visit www.the bin sentry.example for a complete understanding of the product. Specifically visit the home page and the story section of the site.

Target Market(s)

Commercial property owners, Commercial property managers, Reits, sanitation companies, architects, designers, engineers, township building departments, fire marshals, code enforcement departments.

Industry/Entity Type

Commercial

Colors
fbed22
ec1f27
000000
959595

Requirements
Must have
• Must have the black and gold logo provided. The Standard Bin Sentry shown as the dominant seller. Brochure should flow rather then being boxy. The use of color.
• We would like to see the before and after pics. and description feature prominent on the an inside page. This is our selling point.
Nice to have
• We were not happy with the pics. and would like to see the labels removed from the dumpsters. They are a distraction.
• The Standard- Bin Sentry is our primary seller and should be the dominant pic.
Should not have
• Do not include my phone number, should not include the address other then the P.O. Box. Should not include the complete installation instructions.

```html
<!DOCTYPE html>
<html lang="en">
<head>
<meta charset="utf-8">
<title>Bin Sentry Brochure</title>
<link rel="stylesheet" href="https://fonts.googleapis.com/css2?family=Oswald:wght@400;500;600&family=Open+Sans:wght@400;600;700&display=swap">
<style>
:root{
  --yellow:#fbed22;
  --red:#ec1f27;
  --black:#000000;
  --grey:#959595;
  --bg:#c9c9c9;
  --orange:#f26522;
  --gold:#d9b24a;
  --paper:#f2f2f2;
  --ink:#333333;
}
*{box-sizing:border-box;margin:0;padding:0}
html,body{width:822px;height:1200px;overflow:hidden;background:var(--bg)}
body{position:relative;font-family:"Open Sans",Arial,sans-serif;color:var(--ink)}
.spread{position:absolute;left:21px;width:780px;display:flex;box-shadow:0 6px 18px rgba(0,0,0,.25)}
.spread--outside{top:18px;height:560px}
.spread--inside{top:612px;height:570px;background:linear-gradient(#8f8f8f,#a9a9a9)}
.panel{position:relative;width:260px;height:100%;overflow:hidden}
.photo{position:absolute;left:0;width:100%}
.band{position:absolute;left:0;width:100%;height:30px;background:var(--black);display:flex;align-items:center;justify-content:center}
.band__name{font-family:"Oswald",sans-serif;font-weight:600;font-size:15px;letter-spacing:2px;color:var(--gold)}
.label{font-family:"Oswald",sans-serif;font-weight:500;font-size:16px;color:var(--red);display:flex;align-items:center;gap:8px}
.marker{display:inline-block;width:11px;height:11px;background:var(--red);flex:none}
.marker--dark{background:var(--black)}
.copy{font-size:7.4px;line-height:1.38;text-align:justify}
.copy strong{color:var(--red)}
.yellow{background:var(--yellow)}
.card{position:absolute;left:18px;right:18px;background:#fff;box-shadow:0 2px 8px rgba(0,0,0,.35);text-align:center;font-family:"Oswald",sans-serif;font-weight:400;color:#555}
.card h3{font-weight:500;color:var(--red);font-size:19px;margin-bottom:10px}
.card p{font-size:10.5px;line-height:1.35}
.card .hl{color:var(--red)}
.banner{position:absolute;left:0;height:62px;display:flex;align-items:center;font-family:"Oswald",sans-serif;font-weight:500;color:var(--black)}
.tile{position:absolute;background:var(--yellow);display:flex;align-items:center}
.tile__label{writing-mode:vertical-rl;transform:rotate(180deg);font-size:6.5px;font-weight:700;color:#222}
.product-bar{position:absolute;top:283px;left:0;width:100%;height:44px;background:var(--yellow);display:flex;align-items:center;padding-left:16px;gap:10px;font-family:"Oswald",sans-serif;font-size:14.5px;color:#111}
.product-body{position:absolute;top:327px;left:0;width:100%;height:243px;background:var(--paper);padding:10px 14px}
.product-body .copy{font-size:8.4px;line-height:1.4;color:#555}
.product-body .copy+.copy{margin-top:10px}
.guard-img{position:absolute;left:30px;right:30px;bottom:14px;height:95px;border-radius:6px;background:radial-gradient(ellipse at center,#f2d21e 0%,#e9e9e9 70%)}
</style>
</head>
<body>

<section class="spread spread--outside">
  <div class="panel panel--before-after yellow">
    <div class="photo" style="top:0;height:175px;background:linear-gradient(160deg,#b9c1c8,#7d756a 55%,#4e463c)" role="img" aria-label="Damaged masonry dumpster enclosure before installation"></div>
    <div class="band" style="top:175px;justify-content:flex-start;padding-left:22px">
      <span class="label"><span class="marker"></span>BEFORE</span>
    </div>
    <div style="position:absolute;top:212px;left:12px;right:10px">
      <p class="copy"><strong>"The Best Ideas Come from Solving Common Problems"</strong> As commercial real estate owners, we constantly strive to maintain the look and integrity of our properties. The dumpster enclosure is the most overlooked area of a commercial property site and the most likely to be damaged by the carelessness of others. Whenever we developed a new property, little attention was placed on protecting the walls of the dumpster enclosure as well as the control of the placement of the dumpster container on the site. We have used the standard practice of installing bollards within the enclosures, but not surprisingly, the enclosure walls were still being damaged. Needless and costly repairs sparked an idea as simple as the hula hoop. If we could control the removal and the replacement of the dumpster, our problem would be solved.</p>
    </div>
    <div class="photo" style="top:385px;height:175px;background:linear-gradient(170deg,#9aa5ad,#cfc7b6 40%,#2f3d30 70%,#8b8677)" role="img" aria-label="Repaired enclosure with dumpster held by yellow guard after installation"></div>
    <div style="position:absolute;top:385px;right:0;width:95px;height:30px;background:#fff;display:flex;align-items:center;justify-content:center">
      <span class="label" style="color:var(--black)">AFTER<span class="marker marker--dark"></span></span>
    </div>
  </div>

  <div class="panel panel--contact yellow">
    <div class="photo" style="top:0;height:175px;background:radial-gradient(ellipse at 50% 55%,#3b3b3b 0%,#8a8a8a 40%,#d8d8d8 75%)" role="img" aria-label="Sketch style render of a dumpster inside a guard"></div>
    <div class="band" style="top:175px"><span class="band__name">THE BIN SENTRY</span></div>
    <div style="position:absolute;top:212px;left:12px;right:10px">
      <p class="copy"><strong>THE BIN SENTRY™</strong> was developed for the purpose of "Holding the Line Firm". Engineered and patented, THE BIN SENTRY™ has been installed and tested at many of our franchise locations such as Brewline Cafe, Griddle House, Ring Donuts and Fiesta Depot. These locations were chosen because of their excessive turnover of dumpster containers and the wear associated on their enclosures.</p>
      <p class="copy" style="margin-top:8px;text-align:center;font-weight:700;color:#111">The average cost of repairing or replacing a damaged dumpster enclosure is between $1500 - $7000 with no guarantees that the same damage will not occur again.</p>
    </div>
    <div class="card" style="top:335px;height:200px;padding-top:16px">
      <h3>CONTACT &amp; INFO</h3>
      <p>Please visit our website at:<br><span class="hl">thebinsentry.example</span><br>for more detailed information on<br>our products or contact us at:<br><span class="hl">info@thebinsentry.example</span></p>
      <svg width="26" height="18" viewBox="0 0 26 18" style="margin:10px 0 6px"><rect width="26" height="18" fill="var(--red)"/><path d="M0 0 13 10 26 0" fill="none" stroke="#fff" stroke-width="1.6"/></svg>
      <p>P.O. Box 4410 / Cedar Hollow, ST<br>thebinsentry.example</p>
    </div>
  </div>

  <div class="panel panel--story" style="background:linear-gradient(160deg,#2a0d05 0%,#7a1a08 45%,#2b0a04 100%)">
    <div class="photo" style="top:0;height:175px;background:linear-gradient(175deg,#7c6e67,#9aa0a2 45%,#8a8c8c)" role="img" aria-label="Dumpsters behind a chain link gate with yellow guards"></div>
    <div class="band" style="top:175px"><span class="band__name">THE BIN SENTRY</span></div>
    <div class="banner" style="top:205px;width:100%;background:linear-gradient(90deg,var(--yellow),#f7941d 70%,var(--red));padding-left:16px;gap:10px;font-size:21px">
      <span class="marker" style="background:#9a9a9a;width:14px;height:14px"></span>
      Holding the Line Firm
    </div>
    <div class="card" style="top:335px;height:205px;padding:14px 16px 0">
      <h3 style="font-size:18px;margin-bottom:8px">THE BIN SENTRY™</h3>
      <p style="font-size:10px">We are proud to introduce the new line of <span class="hl">THE BIN SENTRY™</span> products. <span class="hl">THE BIN SENTRY™</span> was developed and introduced to property managers and owners to protect their dumpster enclosures from the accidents and carelessness of others. After years of enduring the hassle and enormous cost of repairs, these property managers and owners can now share how they are... <span class="hl">"Holding the Line Firm."</span></p>
    </div>
  </div>
</section>

<section class="spread spread--inside">
  <div class="panel panel--standard">
    <div class="banner" style="top:32px;width:245px;background:linear-gradient(90deg,var(--red),var(--orange) 40%,var(--yellow));clip-path:polygon(0 0,88% 0,100% 50%,88% 100%,0 100%);padding-left:30px;font-size:22px">The Bin Sentry</div>
    <div class="photo" style="top:110px;height:170px;background:radial-gradient(ellipse at 50% 50%,#1f3327 0%,#2d4436 30%,#a89a38 55%,transparent 75%)" role="img" aria-label="Green dumpster inside the standard yellow guard"></div>
    <div class="product-bar"><span class="marker"></span>The Bin Sentry - Standard</div>
    <div class="product-body">
      <p class="copy"><strong>THE BIN SENTRY™ - Standard</strong> is designed to provide maximum protection of masonry enclosures and surrounding structures. Constructed of schedule 40, 3.5" steel tubing and powder coated for protection from the elements.</p>
      <p class="copy"><strong>THE BIN SENTRY™ - Standard</strong> can accommodate containers up to 8 yards.</p>
      <div class="guard-img" role="img" aria-label="Standard yellow steel guard on its own"></div>
    </div>
  </div>

  <div class="panel panel--expandable">
    <div class="banner" style="top:32px;width:100%;background:var(--yellow);padding-left:12px;font-size:20px">Accessories</div>
    <div class="tile" style="top:32px;right:10px;width:86px;height:62px;padding-left:4px;gap:4px">
      <span class="tile__label">Sleeve Anchors</span>
      <div style="width:64px;height:46px;background:radial-gradient(ellipse,#555 0%,#aaa 45%,transparent 70%)" role="img" aria-label="Sleeve anchor bolts"></div>
    </div>
    <div class="photo" style="top:110px;height:170px;background:radial-gradient(ellipse at 55% 45%,#1f3327 0%,#2d4436 25%,#a89a38 50%,transparent 72%)" role="img" aria-label="Dumpster inside the expandable yellow guard"></div>
    <div class="product-bar"><span class="marker"></span>The Bin Sentry - Expandable</div>
    <div class="product-body">
      <p class="copy"><strong>THE BIN SENTRY™ - Expandable</strong> is designed to provide maximum protection of masonry enclosures and surrounding structures. Constructed of schedule 40, 3.5" steel tubing and powder coated for protection from the elements.</p>
      <p class="copy"><strong>THE BIN SENTRY™ - Expandable</strong> can accommodate multiple containers up to 8 yards each.</p>
      <div class="guard-img" role="img" aria-label="Expandable yellow steel guard on its own"></div>
    </div>
  </div>

  <div class="panel panel--expandable-alt">
    <div class="tile" style="top:32px;left:6px;width:60px;height:62px;padding-left:3px;gap:3px">
      <span class="tile__label">Asphalt Anchors</span>
      <div style="width:44px;height:46px;background:radial-gradient(ellipse,#555 0%,#aaa 45%,transparent 70%)" role="img" aria-label="Asphalt anchor spikes"></div>
    </div>
    <div class="tile" style="top:32px;left:72px;width:60px;height:62px;padding-left:3px;gap:3px">
      <span class="tile__label">Touch-Up Paint</span>
      <div style="width:44px;height:46px;background:radial-gradient(ellipse,#f4e04a 0%,#ddd 45%,transparent 70%)" role="img" aria-label="Yellow touch-up spray paint can"></div>
    </div>
    <div class="tile" style="top:32px;left:138px;width:116px;height:62px;padding-left:3px;gap:3px">
      <span class="tile__label">Plow Markers</span>
      <div style="width:100px;height:46px;background:linear-gradient(160deg,transparent 42%,var(--orange) 46%,var(--red) 54%,transparent 58%)" role="img" aria-label="Orange plow marker rods"></div>
    </div>
    <div class="photo" style="top:110px;height:170px;background:radial-gradient(ellipse at 50% 45%,#14213a 0%,#213252 28%,#a89a38 52%,transparent 74%)" role="img" aria-label="Blue dumpster inside the expandable yellow guard"></div>
    <div class="product-bar"><span class="marker"></span>The Bin Sentry - Expandable</div>
    <div class="product-body">
      <p class="copy"><strong>THE BIN SENTRY™ - Expandable</strong> is designed to provide maximum protection of masonry enclosures and surrounding structures. Constructed of schedule 40, 3.5" steel tubing and powder coated for protection from the elements.</p>
      <p class="copy"><strong>THE BIN SENTRY™ - Expandable</strong> can accommodate multiple containers up to 8 yards each.</p>
      <div class="guard-img" role="img" aria-label="Expandable yellow steel guard section on its own"></div>
    </div>
  </div>
</section>

</body>
</html>
```